Mechanical Contractor Business Card and Stationary Design
VoltaCrest Mechanical LLC
Use same font as used in my logo
Helvetica Neue
Simple
Marcus T. Holloway, PE, LEED AP
Managing Member
512-867-0ZAP
mholloway@voltacrestmechanical.com
www.voltacrestmechanical.com
TACLA000048153B
We would like the stationary and business cards to be clean and crisp like the logo. Colors that are applicable are those used in the logo as well as blue and red. The ideal winner will have a catchy and memorable design, while respecting the white space and maintaining a design consistent with the logo.
Logo Font: Helvetica Neue
please message me or contact me with questions.

```html
<!DOCTYPE html>
<html lang="en">
<head>
<meta charset="utf-8">
<title>VoltaCrest Mechanical LLC — Stationery Set</title>
<link rel="stylesheet" href="https://fonts.googleapis.com/css2?family=Arimo:wght@400;700&display=swap">
<style>
  :root{
    --board-top:#4a4a4a;
    --board-bottom:#2e2e2e;
    --paper:#ffffff;
    --paper-shade:#eeeeee;
    --ink:#3c3c3c;
    --ink-soft:#8a8a8a;
    --green:#62b22f;
    --green-dark:#3f8a1c;
    --card-dark:#262626;
    --label:#9a9a9a;
  }
  *{box-sizing:border-box;margin:0;padding:0}
  html,body{width:1200px;height:353px;overflow:hidden}
  body{font-family:"Arimo","Helvetica Neue",Arial,sans-serif;color:var(--ink)}
  .board{position:relative;width:1200px;height:353px;
    background:radial-gradient(ellipse at 50% 40%,var(--board-top),var(--board-bottom));}
  .item{position:absolute;background:var(--paper);box-shadow:0 3px 8px rgba(0,0,0,.45);overflow:hidden}
  .label{position:absolute;font-size:5px;color:var(--label);text-align:center;letter-spacing:.2px}
  .brand{position:absolute;font-weight:700;color:var(--ink);white-space:nowrap;line-height:1}
  .tiny{font-size:3px;line-height:4.4px;color:var(--ink-soft)}
  .band{position:absolute;left:0;bottom:0;width:100%}

  /* business cards */
  .card{width:138px;height:58px}
  .card .brand{left:8px;top:8px;font-size:9px}
  .card .person{position:absolute;left:8px;top:24px}
  .card .person strong{display:block;font-size:4.2px;color:var(--ink)}
  .card .contact{position:absolute;right:8px;top:24px;text-align:right}
  .card-back{background:var(--card-dark)}
  .card-back .brand{left:10px;top:14px;font-size:12px;color:var(--paper)}
  .card-back .sub{position:absolute;left:10px;top:30px;font-size:3.6px;color:var(--ink-soft);letter-spacing:.6px}

  /* letterheads */
  .letter{width:160px;height:276px}
  .letter .brand{right:12px;top:14px;font-size:10px}
  .letter .address{position:absolute;left:12px;top:14px}
  .letter .body{position:absolute;left:12px;top:48px;width:136px;font-size:3.4px;line-height:5px;color:var(--ink-soft)}
  .letter .body p{margin-bottom:4px}
  .letter .body .to{color:var(--ink)}
  .letter .sign{font-style:italic;font-size:7px;color:var(--ink);margin:6px 0 2px}
  .letter .footer{position:absolute;left:12px;bottom:14px;font-size:3px;color:var(--ink-soft)}

  /* compliment slip */
  .slip{width:208px;height:96px}
  .slip .brand{left:10px;top:10px;font-size:10px}
  .slip .contact{position:absolute;right:10px;top:12px;text-align:right}
  .slip .lines{position:absolute;left:10px;top:38px;width:188px}
  .slip .lines span{display:block;height:5px;border-bottom:.5px solid var(--paper-shade)}

  /* envelopes */
  .envelope{width:210px;height:100px;background:var(--paper)}
  .envelope .brand{left:10px;top:10px;font-size:9px}
  .envelope .address{position:absolute;left:10px;top:24px}
</style>
</head>
<body>
<main class="board">

  <section class="item card" style="left:12px;top:115px">
    <div class="brand">VoltaCrest</div>
    <div class="person tiny"><strong>Marcus T. Holloway, PE, LEED AP</strong>Managing Member</div>
    <div class="contact tiny">512-867-0ZAP<br>mholloway@voltacrestmechanical.com<br>www.voltacrestmechanical.com<br>TACLA000048153B</div>
    <svg class="band" width="138" height="12" viewBox="0 0 138 12"><path d="M0 6 Q70 0 138 4 V12 H0Z" fill="var(--green)"/><path d="M0 9 Q70 4 138 8 V12 H0Z" fill="var(--green-dark)"/></svg>
  </section>
  <div class="label" style="left:12px;top:176px;width:138px">Card Front</div>

  <section class="item card" style="left:12px;top:197px">
    <div class="brand">VoltaCrest</div>
    <div class="person tiny"><strong>Marcus T. Holloway, PE, LEED AP</strong>Managing Member</div>
    <div class="contact tiny">512-867-0ZAP<br>mholloway@voltacrestmechanical.com<br>www.voltacrestmechanical.com<br>TACLA000048153B</div>
    <svg class="band" width="138" height="12" viewBox="0 0 138 12"><path d="M0 4 Q70 10 138 3 V12 H0Z" fill="var(--green)"/></svg>
  </section>
  <div class="label" style="left:12px;top:258px;width:138px">Card Front</div>

  <section class="item card card-back" style="left:12px;top:278px;height:50px">
    <div class="brand">VoltaCrest</div>
    <div class="sub">MECHANICAL LLC</div>
  </section>
  <div class="label" style="left:12px;top:331px;width:138px">Card Back</div>

  <section class="item letter" style="left:164px;top:12px">
    <div class="address tiny">1200 Ridge Park Drive<br>Austin, TX 78701<br>512-867-0ZAP</div>
    <div class="brand">VoltaCrest</div>
    <div class="body">
      <p>March 4, 2024</p>
      <p class="to">Jordan Reyes<br>Client Company</p>
      <p>Dear Jordan,</p>
      <p>Thank you for choosing our team for your mechanical project. We look forward to working with you on every phase of the build.</p>
      <p>Sincerely,</p>
      <div class="sign">Marcus T. Holloway</div>
      <p>Managing Member</p>
    </div>
    <div class="footer">www.voltacrestmechanical.com · TACLA000048153B</div>
    <svg class="band" width="160" height="10" viewBox="0 0 160 10"><rect width="160" height="10" fill="var(--green)"/><rect y="7" width="160" height="3" fill="var(--green-dark)"/></svg>
  </section>
  <div class="label" style="left:164px;top:292px;width:160px">Letterhead Page One</div>

  <section class="item letter" style="left:336px;top:12px">
    <div class="address tiny">1200 Ridge Park Drive<br>Austin, TX 78701<br>512-867-0ZAP</div>
    <div class="brand">VoltaCrest</div>
    <div class="body">
      <p>March 4, 2024</p>
      <p class="to">Jordan Reyes<br>Client Company</p>
      <p>Dear Jordan,</p>
      <p>Thank you for choosing our team for your mechanical project. We look forward to working with you on every phase of the build.</p>
      <p>Sincerely,</p>
      <div class="sign">Marcus T. Holloway</div>
      <p>Managing Member</p>
    </div>
    <div class="footer">www.voltacrestmechanical.com · TACLA000048153B</div>
    <svg class="band" width="160" height="10" viewBox="0 0 160 10"><rect width="160" height="10" fill="var(--green)"/></svg>
  </section>
  <div class="label" style="left:336px;top:292px;width:160px">Letterhead Page Two</div>

  <section class="item card" style="left:510px;top:96px;width:100px;height:44px">
    <div class="brand" style="font-size:7px;left:6px;top:6px">VoltaCrest</div>
    <div class="contact tiny" style="right:6px;top:20px">512-867-0ZAP<br>www.voltacrestmechanical.com</div>
    <svg class="band" width="100" height="6" viewBox="0 0 100 6"><rect width="100" height="6" fill="var(--green)"/></svg>
  </section>
  <section class="item card card-back" style="left:620px;top:96px;width:100px;height:44px">
    <div class="brand" style="font-size:9px;left:10px;top:17px">VoltaCrest</div>
  </section>
  <section class="item card" style="left:510px;top:150px;width:100px;height:44px">
    <div class="brand" style="font-size:7px;left:6px;top:6px">VoltaCrest</div>
    <div class="person tiny" style="left:6px;top:20px"><strong>Marcus T. Holloway</strong>Managing Member</div>
    <svg class="band" width="100" height="6" viewBox="0 0 100 6"><rect width="100" height="6" fill="var(--green)"/></svg>
  </section>
  <div class="label" style="left:510px;top:198px;width:210px">Card Set</div>

  <section class="item slip" style="left:512px;top:218px">
    <div class="brand">VoltaCrest</div>
    <div class="contact tiny">1200 Ridge Park Drive<br>Austin, TX 78701<br>www.voltacrestmechanical.com</div>
    <div class="lines"><span></span><span></span><span></span><span></span><span></span></div>
    <svg class="band" width="208" height="10" viewBox="0 0 208 10"><path d="M0 4 Q104 0 208 4 V10 H0Z" fill="var(--green)"/></svg>
  </section>
  <div class="label" style="left:512px;top:318px;width:208px">Compliment Slip</div>

  <section class="item envelope" style="left:746px;top:110px">
    <div class="brand">VoltaCrest</div>
    <div class="address tiny">1200 Ridge Park Drive<br>Austin, TX 78701</div>
    <svg class="band" width="210" height="10" viewBox="0 0 210 10"><rect width="210" height="10" fill="var(--green)"/></svg>
  </section>
  <section class="item envelope" style="left:776px;top:228px;width:170px;height:70px">
    <div class="brand" style="font-size:7px">VoltaCrest</div>
    <svg class="band" width="170" height="8" viewBox="0 0 170 8"><rect width="170" height="8" fill="var(--green)"/></svg>
  </section>
  <div class="label" style="left:746px;top:304px;width:210px">Envelope Front</div>

  <section class="item envelope" style="left:976px;top:120px;height:110px;background:var(--paper-shade)">
    <svg width="210" height="110" viewBox="0 0 210 110">
      <path d="M0 0 L105 62 L210 0 Z" fill="var(--paper)"/>
      <path d="M0 110 L105 55 L210 110 Z" fill="#f6f6f6"/>
      <path d="M0 0 L105 62 L210 0 L210 10 L105 70 L0 10 Z" fill="var(--green)" opacity=".9"/>
    </svg>
  </section>
  <section class="item envelope" style="left:990px;top:240px;width:180px;height:60px;background:var(--paper-shade)">
    <svg width="180" height="60" viewBox="0 0 180 60">
      <path d="M0 0 L90 34 L180 0 Z" fill="var(--paper)"/>
      <path d="M0 0 L90 34 L180 0 L180 6 L90 40 L0 6 Z" fill="var(--green)"/>
    </svg>
  </section>
  <div class="label" style="left:976px;top:304px;width:210px">Envelope Back</div>

</main>
</body>
</html>
```